Card design for Heating and Cooling company

this is for a heating and cooling company we recently updated our logo and need to update our cards. We attached our logo so you can incorporate it into the card. We specialize in residential and commercial furnace and air condition repairs. Have been in business since 2014.

Phone number 555.284.9137

We need the following phrases
:Repairs, Installations, and maintenance
:Quality work at reasonable prices
:residential/commercial
:Licensed &Insured
:Email Pinegrovehvac47@mailbox-example.com
Name: Teodor K (Ted)
Also on back side I would like my logo with wording :Thank you for your business and refferal

Industry/Entity Type

Hvac

Contact Information for Business Card

:residential/commercial
:Licensed & Insured
Name: Teodor K (Ted)
Number:555.284.9136

Requirements
Must have
• Blue and red colors
Nice to have
• Maybe a pic of a furnace or air conditioner

```html
<!DOCTYPE html>
<html lang="en">
<head>
<meta charset="utf-8">
<title>Frostline Heating &amp; Cooling – Business Cards</title>
<link rel="stylesheet" href="https://fonts.googleapis.com/css2?family=Montserrat:wght@600;700;800&family=Mulish:wght@400;500;700&display=swap">
<style>
  :root{
    --bg:#d9dadc;
    --paper:#f3f3f3;
    --blue:#3592cf;
    --blue-light:#6fb5e2;
    --red:#e0262b;
    --orange:#f0761f;
    --ink:#1d1d1d;
    --rule:#8a8a8a;
  }
  *{box-sizing:border-box;margin:0;padding:0}
  html,body{width:1200px;height:1021px;overflow:hidden}
  body{background:var(--bg);position:relative;font-family:"Mulish",sans-serif;color:var(--ink)}

  .card{position:absolute;box-shadow:0 10px 26px rgba(0,0,0,.22);overflow:hidden}

  /* Front (portrait) */
  .card-front{left:70px;top:160px;width:400px;height:700px;background:linear-gradient(160deg,#fafafa,#e9e9e9);display:flex;flex-direction:column}
  .strip{height:46px;display:flex;align-items:center;justify-content:center;color:#fff;font-family:"Mulish",sans-serif;font-weight:500;font-size:19px;letter-spacing:2px}
  .strip-top{background:var(--blue)}
  .strip-bottom{background:var(--red);margin-top:auto}
  .front-body{flex:1;display:flex;flex-direction:column;align-items:center;text-align:center;padding:58px 30px 0}
  .brand{display:flex;align-items:center;gap:14px;margin-bottom:40px}
  .brand-dot{width:22px;height:22px;border-radius:50%;background:var(--blue)}
  .brand-name{font-family:"Montserrat",sans-serif;font-weight:800;color:var(--ink);font-size:38px;line-height:1.05;text-transform:uppercase}
  .brand-name small{display:block;font-size:13px;letter-spacing:5px;margin-top:4px}
  .services{font-size:19px;line-height:1.35}
  .services .sep{color:var(--red)}
  .contact-name{margin-top:70px;font-family:"Montserrat",sans-serif;font-weight:700;font-size:25px;color:var(--blue)}
  .contact-name .nick{color:var(--red)}
  .divider{width:36px;height:1px;background:var(--rule);margin:22px auto}
  .contact-lines{font-size:19px;line-height:1.45}

  /* Back (landscape) */
  .card-back{left:530px;top:330px;width:620px;height:354px;background:var(--red)}
  .back-top{position:absolute;left:0;top:0;width:100%;height:124px;background:radial-gradient(ellipse at 50% 100%,var(--blue-light) 0%,var(--blue) 70%)}
  .back-band{position:absolute;left:0;top:124px;width:100%;height:62px;background:var(--paper);display:flex;align-items:flex-end;justify-content:center;padding-bottom:8px}
  .back-bottom{position:absolute;left:0;top:186px;width:100%;height:168px;background:radial-gradient(ellipse at 50% 0%,#f6a11d 0%,var(--orange) 25%,var(--red) 65%)}
  .thanks{font-family:"Montserrat",sans-serif;font-weight:800;font-size:15px;letter-spacing:1px;color:var(--blue);text-transform:uppercase}
  .thanks em{font-style:normal;color:var(--red)}
  .back-brand{position:absolute;left:0;top:36px;width:100%;text-align:center;font-family:"Montserrat",sans-serif;font-weight:800;font-size:40px;color:#fff;letter-spacing:3px;text-transform:uppercase}
</style>
</head>
<body>
  <section class="card card-front">
    <div class="strip strip-top">LICENSED &amp; INSURED</div>
    <div class="front-body">
      <div class="brand">
        <span class="brand-dot"></span>
        <div class="brand-name">Frostline<small>Heating &amp; Cooling</small></div>
      </div>
      <p class="services">Repairs <span class="sep">|</span> Installations <span class="sep">|</span> Maintenance<br>Quality work at reasonable prices</p>
      <p class="contact-name">Teodor K <span class="nick">(Ted)</span></p>
      <div class="divider"></div>
      <p class="contact-lines">555.284.9137<br>Pinegrovehvac47@mailbox-example.com</p>
    </div>
    <div class="strip strip-bottom">RESIDENTIAL / COMMERCIAL</div>
  </section>

  <section class="card card-back">
    <div class="back-top"></div>
    <div class="back-bottom"></div>
    <div class="back-band"><p class="thanks"><em>Thank you</em> for your business and refferal</p></div>
    <div class="back-brand">Frostline</div>
  </section>
</body>
</html>
```